Staffing and Consulting Service Company needs Business Cards

We need to have business cards for our business. You can check our website www.talvrenix.com to see the branding we are using. The logo is in the website.
We use a tag line Talent & Advisory Services For Growing Teams.
We use different blues in the logo and we use the red for the Company name.
As you can see in the website there is a gradient in the bottom part of each page that includes some of the dots we use for the logo.
We will need the following fields on the design:
Company Name
Employee Name
Title
Address
Tel
Email
Website
Can be Single or Double Sided
There is no preference for single or double sided.
Target Market(s)
Companies in need of IT staffing and IT consulting services
Industry/Entity Type
Business
Look and feel

```html
<!DOCTYPE html>
<html lang="en">
<head>
<meta charset="utf-8">
<title>Talvrenix Business Card</title>
<link rel="stylesheet" href="https://fonts.googleapis.com/css2?family=Lato:wght@400;700&display=swap">
<style>
  :root {
    --backdrop: #a3a4a7;
    --card-top-light: #ffffff;
    --card-top-tint: #c9e1ec;
    --band-deep: #1f3f7e;
    --band-dark: #22386a;
    --brand-red: #8b4a4f;
    --brand-navy: #233a6a;
    --ink-navy: #243f6e;
    --text-light: #ffffff;
  }
  * { box-sizing: border-box; margin: 0; padding: 0; }
  html, body {
    width: 1200px;
    height: 736px;
    overflow: hidden;
    background: var(--backdrop);
    font-family: "Lato", Arial, sans-serif;
  }
  .business-card {
    position: absolute;
    left: 180px;
    top: 128px;
    width: 840px;
    height: 480px;
    overflow: hidden;
    box-shadow: 0 10px 30px rgba(0,0,0,0.25);
  }
  .card-face {
    position: absolute;
    inset: 0 0 176px 0;
    background: linear-gradient(120deg, var(--card-top-light) 0%, #e6f1f6 35%, var(--card-top-tint) 100%);
  }
  .contact-band {
    position: absolute;
    left: 0; right: 0; bottom: 0;
    height: 176px;
    background: linear-gradient(100deg, var(--band-deep) 0%, #24488a 45%, var(--band-dark) 100%);
  }
  .brand {
    position: absolute;
    left: 50px;
    top: 68px;
  }
  .brand-name {
    font-weight: 400;
    font-size: 38px;
    letter-spacing: 1px;
    line-height: 1;
    color: var(--brand-red);
  }
  .brand-tagline {
    margin-top: 6px;
    font-size: 11.5px;
    color: var(--brand-navy);
  }
  .person {
    position: absolute;
    right: 46px;
    top: 222px;
    text-align: right;
    color: var(--ink-navy);
  }
  .person-name { font-size: 29px; line-height: 1.2; }
  .person-title { font-size: 22px; margin-top: 8px; }
  .contact-list {
    position: absolute;
    right: 44px;
    bottom: 34px;
    list-style: none;
    text-align: right;
    color: var(--text-light);
    font-size: 23px;
    line-height: 1.45;
  }
  .contact-list .divider { margin: 0 6px; }
</style>
</head>
<body>
  <article class="business-card">
    <div class="card-face" role="img" aria-label="Soft light-blue gradient with a pattern of pale circles"></div>
    <div class="contact-band" role="img" aria-label="Deep blue band with a pattern of faint circles"></div>

    <header class="brand">
      <div class="brand-name">TALVRENIX</div>
      <div class="brand-tagline">Talent &amp; Advisory Services For Growing Teams</div>
    </header>

    <section class="person">
      <p class="person-name">Jhon Doe</p>
      <p class="person-title">Chief Executive Officer</p>
    </section>

    <ul class="contact-list">
      <li class="contact-address">4810 NW 98th Lane Coral Springs, FL 33076</li>
      <li class="contact-phone">Tel: (954) 555-0172</li>
      <li class="contact-web">Email: resume@talvrenix.com<span class="divider">&bull;</span>www.talvrenix.com</li>
    </ul>
  </article>
</body>
</html>
```